Online plant nursery needs3 seperate slides for a intro web site slide slide show

We need 3 slide graphics / banners measurments should be 960wide 540 tall and 2mb or smaller. We are an online mail order nursery that focuses sales on Peonies.
Slide 1: Use faded out photos of Peony Garden with many flowers just budding. Our logo and the Words "A Lost Spring is Never Found Again". try to use our logo in a small small watermark on all slides.
Slide 2: Use your own creativity for the slide.... message should say "Free Shipping"
Slide 3: Use your own creativity for the slide .... messgae "Shop Our Other Items". To see site it will be used on go to http://k4817395.bwterxplcuha.trial52.shopvendra.com/

Target Market(s)

home owners age 30 - 65.

Industry/Entity Type

Nursery

Requirements
Must have
• must transition well.
Should not have
• can not be larger than 2MB per file

```html
<!DOCTYPE html>
<html lang="en">
<head>
<meta charset="utf-8">
<title>A Lost Spring is Never Found Again</title>
<link rel="stylesheet" href="https://fonts.googleapis.com/css2?family=Yellowtail&family=Open+Sans:wght@400&display=swap">
<style>
  :root {
    --bud-red: #c8404f;
    --bud-pink: #d9677a;
    --leaf-green: #6e8e4c;
    --leaf-deep: #3f6131;
    --haze: rgba(120, 110, 110, 0.42);
    --headline: #ffffff;
    --headline-glow: rgba(90, 20, 40, 0.45);
    --mark: rgba(214, 150, 60, 0.62);
  }
  html, body {
    margin: 0;
    padding: 0;
    width: 1200px;
    height: 675px;
    overflow: hidden;
    background: #ffffff;
  }
  .slide {
    position: relative;
    width: 1200px;
    height: 675px;
    overflow: hidden;
  }
  .slide__photo {
    position: absolute;
    inset: 0;
    background:
      radial-gradient(ellipse 180px 130px at 8% 20%, var(--bud-red), transparent 70%),
      radial-gradient(ellipse 200px 140px at 30% 38%, var(--bud-pink), transparent 70%),
      radial-gradient(ellipse 220px 150px at 62% 48%, var(--bud-red), transparent 70%),
      radial-gradient(ellipse 200px 140px at 88% 22%, var(--bud-pink), transparent 70%),
      radial-gradient(ellipse 180px 140px at 10% 78%, var(--bud-red), transparent 70%),
      radial-gradient(ellipse 200px 150px at 72% 80%, var(--bud-pink), transparent 70%),
      radial-gradient(ellipse 160px 120px at 92% 62%, var(--bud-red), transparent 70%),
      linear-gradient(160deg, var(--leaf-green) 0%, var(--leaf-deep) 55%, var(--leaf-green) 100%);
  }
  .slide__haze {
    position: absolute;
    inset: 0;
    background: var(--haze);
  }
  .brand-mark {
    position: absolute;
    display: flex;
    align-items: center;
    gap: 10px;
    font-family: "Open Sans", sans-serif;
    font-size: 20px;
    font-weight: 400;
    color: var(--mark);
    white-space: nowrap;
  }
  .brand-mark__dot {
    width: 62px;
    height: 62px;
    border-radius: 50%;
    background: var(--mark);
    opacity: 0.55;
  }
  .headline {
    position: absolute;
    left: 0;
    right: 0;
    top: 300px;
    margin: 0;
    text-align: center;
    font-family: "Yellowtail", cursive;
    font-weight: 400;
    font-size: 66px;
    line-height: 1;
    color: var(--headline);
    text-shadow: 0 2px 6px var(--headline-glow);
  }
</style>
</head>
<body>
  <main class="slide">
    <div class="slide__photo" role="img" aria-label="Faded photograph of a peony garden full of pink and red buds just starting to open among green leaves"></div>
    <div class="slide__haze"></div>

    <div class="brand-mark" style="left:25px; top:42px;"><span class="brand-mark__dot"></span>Meadow Bloom</div>
    <div class="brand-mark" style="left:468px; top:46px;"><span class="brand-mark__dot"></span>Meadow Bloom</div>
    <div class="brand-mark" style="left:881px; top:46px;"><span class="brand-mark__dot"></span>Meadow Bloom</div>
    <div class="brand-mark" style="left:447px; top:180px;"><span class="brand-mark__dot"></span>Meadow Bloom</div>
    <div class="brand-mark" style="left:460px; top:418px;"><span class="brand-mark__dot"></span>Meadow Bloom</div>
    <div class="brand-mark" style="left:38px; top:550px;"><span class="brand-mark__dot"></span>Meadow Bloom</div>
    <div class="brand-mark" style="left:506px; top:543px;"><span class="brand-mark__dot"></span>Meadow Bloom</div>
    <div class="brand-mark" style="left:897px; top:538px;"><span class="brand-mark__dot"></span>Meadow Bloom</div>

    <h1 class="headline">A Lost Spring is Never Found Again</h1>
  </main>
</body>
</html>
```